Bloom Wardrobe Co relaunch: brand, logo and website redesign

Bloom Wardrobe Co www.bloomwardrobeco.com is relaunching to focus on empowering style advice, e books and courses.
We need a new logo, brand identity and website which reflects this change.
The structure of the site and pages have been completed http://dev1.bloomwardrobeco.com/
but we need to update the brand look and feel
Please read the full brief, uploaded, before submitting your designs.

Target Market(s)

Women, primarily aged 28-45, English speaking USA and UK
Ambitious and determined. Looking for solutions. Open to self-improvement.
Maybe not as confident with style and body image as other parts of their life.

Logo Text

Brand name Bloom Wardrobe Co Strapline version 1: Shine in your own way Strapline version 2: Rise higher Logo/graphical icon for use with/without text

Number of Pages Required

3 page

Font styles to use
Sans Serif

Requirements
Must have
• 1. Web designs for home page, a channel page and advice page (see attached brief)
Web designs must be consistent with new website design navigation, and page structure http://dev1.bloomwardrobeco.com/
2. Web style guide to include colour palettes/system; web fonts, icons, illustrations and guidelines/examples free stock photography. see Mindmap upload for example of colour pallette we like.
Nice to have
• Ebook front covers
Quiz promotions
Course promotions
Other web pages
Social media pages eg Facebook, Instagram,Twitter
Should not have
• Paid photography or photos where don’t have the rights

```html
<!DOCTYPE html>
<html lang="en">
<head>
<meta charset="utf-8">
<title>Bloom Wardrobe Co – Home</title>
<link href="https://fonts.googleapis.com/css2?family=Poppins:wght@300;400;500;600&family=Dancing+Script:wght@500;600&display=swap" rel="stylesheet">
<style>
:root{
  --pink:#e4677a;
  --pink-deep:#d9546a;
  --pink-soft:#f1b9c1;
  --blue:#1b8ec9;
  --mist:#d6e4e8;
  --ink:#2f2f33;
  --grey:#77777d;
  --white:#ffffff;
  --footer:#2a2a2d;
  --script:"Dancing Script",cursive;
  --sans:"Poppins",sans-serif;
}
*{box-sizing:border-box;margin:0;padding:0}
html,body{width:1200px;height:5088px;overflow:hidden}
body{font-family:var(--sans);color:var(--ink);background:var(--white)}
section,header,footer{position:relative;width:1200px;overflow:hidden}
.script{font-family:var(--script);font-weight:600}
.btn{display:inline-block;background:var(--pink);color:var(--white);font-size:13px;font-weight:500;letter-spacing:1px;padding:11px 30px;border-radius:22px}
.btn-outline{background:transparent;border:2px solid var(--white)}
.photo{border-radius:2px}

/* header */
.site-header{height:90px;display:flex;align-items:center;padding:0 80px;justify-content:space-between}
.brand{display:flex;align-items:center;gap:10px;font-weight:600;font-size:20px;color:var(--blue)}
.brand-dot{width:14px;height:14px;border-radius:50%;background:var(--pink)}
.main-nav{display:flex;align-items:center;gap:30px;font-size:13px;font-weight:500;letter-spacing:1px}
.main-nav .active{color:var(--pink)}
.nav-icons{display:flex;gap:18px;margin-left:14px}

/* hero */
.hero{height:490px;background:var(--pink)}
.hero-photo{position:absolute;left:250px;top:30px;width:850px;height:460px;border:6px solid rgba(255,255,255,.85);border-bottom:0;background:linear-gradient(90deg,#f3d5dc 0%,#e8eef2 30%,#7da6c6 55%,#f0c8c1 75%,#3c4a5e 100%)}
.hero-copy{position:absolute;left:300px;top:170px;color:var(--white)}
.hero-copy .eyebrow{font-size:30px;font-weight:300;margin-bottom:8px}
.hero-copy h1{font-size:58px;line-height:1.05;margin-bottom:30px}

/* about */
.about{height:570px}
.about-photo{position:absolute;left:160px;top:40px;width:300px;height:500px;background:linear-gradient(180deg,#eef0f2 0%,#c9d0da 40%,#2b4a94 70%,#1f2430 100%)}
.about-copy{position:absolute;left:560px;top:110px;width:460px;text-align:center}
.about-copy h2{font-size:52px;font-weight:500;color:var(--ink)}
.about-copy .name{font-size:56px;line-height:1;margin-bottom:20px}
.about-copy p{font-size:13px;color:var(--grey);line-height:1.7;margin-bottom:12px}

/* advice */
.advice{height:530px;background:var(--pink-soft);text-align:center}
.section-title{font-size:60px;padding-top:50px}
.advice .section-title{color:var(--white)}
.advice-cards{display:flex;gap:24px;justify-content:center;margin-top:40px}
.advice-card{width:210px;background:var(--white);box-shadow:0 6px 16px rgba(0,0,0,.12);text-align:left}
.advice-card .photo{height:160px}
.advice-card h3{font-size:17px;font-weight:500;padding:14px 16px 4px}
.advice-card p{font-size:11px;color:var(--grey);padding:0 16px 22px}

/* courses */
.courses{height:470px}
.courses-copy{position:absolute;left:190px;top:90px;width:360px;text-align:center}
.courses-copy h2{font-size:58px;margin-bottom:18px}
.courses-copy p{font-size:12px;color:var(--grey);line-height:1.7;margin-bottom:12px}
.video-frame{position:absolute;left:640px;top:120px;width:360px;height:215px;border:4px solid var(--pink);transform:translate(14px,14px)}
.video{position:absolute;left:620px;top:105px;width:370px;height:220px;background:linear-gradient(135deg,#c9a089,#efe3dc 45%,#6f8fb0);box-shadow:0 6px 18px rgba(0,0,0,.18)}
.video-title{position:absolute;left:0;top:0;right:0;padding:10px 14px;font-size:12px;color:var(--white);background:rgba(0,0,0,.45)}
.video svg{position:absolute;left:155px;top:80px}

/* quizzes */
.quizzes{height:710px;background:var(--blue);text-align:center;color:var(--white)}
.quizzes .section-title{padding-top:40px}
.quizzes .sub{font-size:30px;font-weight:300;margin-top:-6px}
.quiz-cards{display:flex;gap:30px;justify-content:center;margin-top:36px}
.quiz-card{width:300px;background:var(--white);color:var(--ink);text-align:left;box-shadow:0 8px 20px rgba(0,0,0,.2)}
.quiz-card .photo{height:210px}
.quiz-card h3{font-size:17px;font-weight:500;padding:18px 20px 6px}
.quiz-card p{font-size:11px;color:var(--grey);line-height:1.6;padding:0 20px 18px}
.quiz-card .btn{margin:0 20px 26px;padding:8px 22px;font-size:11px}

/* ebooks */
.ebooks{height:620px}
.ebooks-copy{position:absolute;left:190px;top:190px;width:380px;text-align:center}
.ebooks-copy h2{font-size:58px;margin-bottom:18px}
.ebooks-copy p{font-size:12px;color:var(--grey);line-height:1.7;margin-bottom:12px}
.book{position:absolute;left:680px;top:90px;width:310px;height:430px;background:linear-gradient(180deg,#f4f1ee 0%,#e9d98a 45%,#cf3c4b 80%,#2d2d35 100%);box-shadow:10px 12px 22px rgba(0,0,0,.28)}

/* blogs */
.blogs{height:660px;background:var(--mist);text-align:center}
.blog-cards{display:flex;gap:30px;justify-content:center;margin-top:40px}
.blog-card{width:290px;background:var(--white);text-align:left;box-shadow:0 6px 16px rgba(0,0,0,.1)}
.blog-card .photo{height:200px}
.blog-card h3{font-size:17px;font-weight:600;line-height:1.35;padding:18px 18px 8px}
.blog-card p{font-size:11px;color:var(--grey);line-height:1.6;padding:0 18px 24px}

/* instagram */
.instagram{height:580px;text-align:center}
.insta-grid{display:grid;grid-template-columns:repeat(5,150px);grid-auto-rows:150px;gap:6px;justify-content:center;margin-top:40px}

/* footer */
.site-footer{height:368px;background:var(--footer);color:#c9c9cc;border-top:8px solid var(--pink)}
.footer-links{position:absolute;left:280px;top:50px;font-size:12px;line-height:2.1;list-style:none}
.footer-brand{position:absolute;left:0;right:0;top:60px;text-align:center}
.footer-brand .brand{justify-content:center;color:var(--white)}
.socials{display:flex;gap:14px;justify-content:center;margin-top:20px}
.socials span{width:22px;height:22px;border-radius:50%;background:#6e6e74}
.copyright{font-size:11px;margin-top:18px}
.footer-legal{position:absolute;left:840px;top:120px;font-size:12px;line-height:2.1;list-style:none}
</style>
</head>
<body>

<header class="site-header">
  <div class="brand"><span class="brand-dot"></span>Bloom Wardrobe Co</div>
  <nav class="main-nav">
    <span class="active">HOME</span><span>ABOUT</span><span>ADVICE</span><span>COURSES</span><span>QUIZZES</span><span>EBOOKS</span><span>BLOG</span>
    <span class="nav-icons">
      <svg width="18" height="18" viewBox="0 0 24 24" fill="none" stroke="#2f2f33" stroke-width="2"><path d="M3 4h3l2 11h11l2-8H7"/><circle cx="10" cy="20" r="1.5"/><circle cx="17" cy="20" r="1.5"/></svg>
      <svg width="18" height="18" viewBox="0 0 24 24" fill="none" stroke="#2f2f33" stroke-width="2"><circle cx="10" cy="10" r="7"/><path d="M15 15l6 6"/></svg>
    </span>
  </nav>
</header>

<section class="hero">
  <div class="hero-photo photo" role="img" aria-label="Clothes hanging on a rail against a pink wall"></div>
  <div class="hero-copy">
    <p class="eyebrow">New Course</p>
    <h1 class="script">How to Organise<br>Your Wardrobe</h1>
    <span class="btn btn-outline">LEARN MORE</span>
  </div>
</section>

<section class="about">
  <div class="about-photo photo" role="img" aria-label="Portrait of the stylist in a blue blouse"></div>
  <div class="about-copy">
    <h2 class="script">About</h2>
    <p class="name script">Clara Westbrook</p>
    <p>I help women find clothes that fit their shape, colouring and lifestyle, so getting dressed feels easy and joyful every single day.</p>
    <p>Stylist, author and course creator sharing simple advice for real wardrobes.</p>
    <span class="btn">READ MORE</span>
  </div>
</section>

<section class="advice">
  <h2 class="section-title script">Style Advice</h2>
  <div class="advice-cards">
    <article class="advice-card"><div class="photo" role="img" aria-label="Colourful flower close-up" style="background:linear-gradient(135deg,#f2c230,#e2487a 55%,#3aa0c8)"></div><h3>Colour Guides</h3><p>Find the shades that flatter you most.</p></article>
    <article class="advice-card"><div class="photo" role="img" aria-label="Sewing tools and fabric" style="background:linear-gradient(135deg,#e8a83c,#b9543e 60%,#5c3a2c)"></div><h3>Shape Guides</h3><p>Dress for your shape with ease.</p></article>
    <article class="advice-card"><div class="photo" role="img" aria-label="Woman in a light dress" style="background:linear-gradient(135deg,#efe6da,#d8c2a2 60%,#a9b3a0)"></div><h3>Measurement Guides</h3><p>Measure yourself the simple way.</p></article>
    <article class="advice-card"><div class="photo" role="img" aria-label="Bride in a white gown" style="background:linear-gradient(135deg,#f6f0ea,#e4d4c8 60%,#c7b4a6)"></div><h3>Wedding Style</h3><p>Bridal looks for every guest.</p></article>
  </div>
</section>

<section class="courses">
  <div class="courses-copy">
    <h2 class="script">Courses</h2>
    <p>Short online courses that guide you step by step through your wardrobe, your shape and your colours at your own pace.</p>
    <p>Each lesson is clear, practical and ready to use the moment you finish watching it at home.</p>
    <span class="btn">VIEW MORE</span>
  </div>
  <div class="video-frame"></div>
  <div class="video" role="img" aria-label="Course video still of the stylist beside a clothes rail">
    <div class="video-title">Clara Westbrook – Personal Stylist &amp; Course</div>
    <svg width="60" height="60" viewBox="0 0 60 60"><circle cx="30" cy="30" r="28" fill="rgba(0,0,0,.55)"/><path d="M24 18l18 12-18 12z" fill="#fff"/></svg>
  </div>
</section>

<section class="quizzes">
  <h2 class="section-title script">Quizzes</h2>
  <p class="sub">Discover Your Style DNA</p>
  <div class="quiz-cards">
    <article class="quiz-card"><div class="photo" role="img" aria-label="Fashion sketches of outfits" style="background:linear-gradient(135deg,#f3ece4,#e4b9b0 50%,#9bb6d0)"></div><h3>Style Quiz</h3><p>Take this short quiz to discover your true style personality and the looks that suit you best.</p><span class="btn">START</span></article>
    <article class="quiz-card"><div class="photo" role="img" aria-label="Bridal bouquet of roses" style="background:linear-gradient(135deg,#f4e7e2,#e7a7b0 50%,#b9c79e)"></div><h3>Wedding Quiz</h3><p>Answer a few questions to find the wedding dress shape made for your figure and day.</p><span class="btn">START</span></article>
    <article class="quiz-card"><div class="photo" role="img" aria-label="Mystery figure with a question mark" style="background:linear-gradient(180deg,#e6e6e8,#2a2a2e)"></div><h3>Neckline Quiz</h3><p>Find out which necklines balance your face, shoulders and bust for a polished look.</p><span class="btn">START</span></article>
  </div>
</section>

<section class="ebooks">
  <div class="ebooks-copy">
    <h2 class="script">eBooks</h2>
    <p>Practical guides you can read anywhere, packed with tips, checklists and outfit ideas for every season.</p>
    <p>Download today and start building a wardrobe you love to wear.</p>
    <span class="btn">VIEW MORE</span>
  </div>
  <div class="book" role="img" aria-label="eBook cover with the stylist in a yellow top"></div>
</section>

<section class="blogs">
  <h2 class="section-title script">Blogs</h2>
  <div class="blog-cards">
    <article class="blog-card"><div class="photo" role="img" aria-label="Couple at a formal event" style="background:linear-gradient(135deg,#d9dde3,#2c5fa8 55%,#1f2633)"></div><h3>Lady Ashford dressed in an electric blue dress!</h3><p>A striking colour choice at a recent charity evening proved once again that bold blue works beautifully.</p></article>
    <article class="blog-card"><div class="photo" role="img" aria-label="Woman in a velvet dress" style="background:linear-gradient(135deg,#e9e3ea,#8e3f7a 55%,#3d2a40)"></div><h3>Objects of desire: Velvet dresses!</h3><p>Rich, soft and glamorous, velvet is back this season and here is how to wear it well.</p></article>
    <article class="blog-card"><div class="photo" role="img" aria-label="Woman in a party dress" style="background:linear-gradient(135deg,#f2efec,#d7c8bd 55%,#9a8a80)"></div><h3>How to dress right for your age during the festive and party season!</h3><p>Party season is here, so here are our top tips for looking polished and feeling confident at any age.</p></article>
  </div>
</section>

<section class="instagram">
  <h2 class="section-title script">Instagram</h2>
  <div class="insta-grid">
    <div class="photo" role="img" aria-label="Friends in colourful outfits" style="background:linear-gradient(135deg,#e88fa0,#c33d5e)"></div>
    <div class="photo" role="img" aria-label="Woman in a summer dress" style="background:linear-gradient(135deg,#d8b49a,#8b5a43)"></div>
    <div class="photo" role="img" aria-label="Woman with long hair" style="background:linear-gradient(135deg,#c9a88e,#5d3e33)"></div>
    <div class="photo" role="img" aria-label="Flowers and accessories" style="background:linear-gradient(135deg,#f2d2d8,#c97a8a)"></div>
    <div class="photo" role="img" aria-label="Woman in a wide hat" style="background:linear-gradient(135deg,#e9e4df,#7b6a5e)"></div>
    <div class="photo" role="img" aria-label="Woman in a black dress" style="background:linear-gradient(135deg,#b9b3b0,#2d2b2e)"></div>
    <div class="photo" role="img" aria-label="Woman in a red coat" style="background:linear-gradient(135deg,#e0a39b,#a3323a)"></div>
    <div class="photo" style="background:#f1f1f3"></div>
    <div class="photo" role="img" aria-label="Couple in evening wear" style="background:linear-gradient(135deg,#b7c5d8,#2f3e5c)"></div>
    <div class="photo" role="img" aria-label="Woman in a blue top" style="background:linear-gradient(135deg,#cfe0ee,#3b78b6)"></div>
  </div>
</section>

<footer class="site-footer">
  <ul class="footer-links"><li>Home</li><li>Style Advice</li><li>Courses</li><li>Quizzes</li><li>eBooks</li><li>Blog</li></ul>
  <div class="footer-brand">
    <div class="brand"><span class="brand-dot"></span>Bloom Wardrobe Co</div>
    <div class="socials"><span></span><span></span><span></span><span></span></div>
    <p class="copyright">Copyright © 2024 Bloom Wardrobe Co</p>
  </div>
  <ul class="footer-legal"><li>Privacy Policy</li><li>Terms &amp; Conditions</li></ul>
</footer>

</body>
</html>
```